need to update our new address on letterhead and business cards. Also open to
a redesign and logo in the near future as we are changing our name. New address is Bramcote Commerce Court, 781 Ashgrove Street, Cheshire, CT 06287

Target Market(s)

35-75 yrs of age

Industry/Entity Type

Business

Requirements
Nice to have
• We are a financial firm so this need to look impressive and classy

```html
<!DOCTYPE html>
<html lang="en">
<head>
<meta charset="utf-8">
<title>Wrenfield Financial – Envelope</title>
<link rel="stylesheet" href="https://fonts.googleapis.com/css2?family=Alegreya:wght@500&family=Arimo:wght@400;700&display=swap">
<style>
  :root {
    --navy: #1f2d4f;
    --stone: #d9d3c8;
    --paper: #ffffff;
  }
  * { margin: 0; padding: 0; box-sizing: border-box; }
  html, body {
    width: 1200px;
    height: 497px;
    overflow: hidden;
    background: var(--paper);
  }
  .envelope {
    position: relative;
    width: 1200px;
    height: 497px;
    background: var(--paper);
  }
  .brand-name {
    position: absolute;
    left: 54px;
    top: 30px;
    width: 422px;
    font-family: "Alegreya", Georgia, serif;
    font-weight: 500;
    font-size: 48px;
    line-height: 1;
    color: var(--navy);
    letter-spacing: 0.3px;
    white-space: nowrap;
  }
  .return-address {
    position: absolute;
    left: 54px;
    top: 86px;
    width: 420px;
    height: 74px;
    background: var(--stone);
    box-shadow: 4px 4px 0 var(--navy);
    padding: 5px 11px;
    font-family: "Arimo", Arial, sans-serif;
    font-style: normal;
    color: var(--navy);
  }
  .return-address .line {
    display: block;
    font-size: 12px;
    line-height: 16px;
  }
  .return-address .web {
    display: block;
    margin-top: 4px;
    font-size: 12px;
    line-height: 14px;
    font-weight: 700;
  }
  .corner-frame {
    position: absolute;
    left: 0;
    top: 0;
  }
  .rule-navy { stroke: var(--navy); }
  .rule-stone { stroke: var(--stone); }
</style>
</head>
<body>
  <main class="envelope">
    <div class="brand-name">Wrenfield Financial</div>

    <address class="return-address">
      <span class="line">Bramcote Commerce Court,</span>
      <span class="line">781 Ashgrove Street,</span>
      <span class="line">Cheshire, CT 06287</span>
      <span class="web">www.wrenfieldfinancialsvcs.com</span>
    </address>

    <svg class="corner-frame" width="1200" height="497" viewBox="0 0 1200 497" aria-hidden="true">
      <polyline class="rule-navy" points="1146,188 1146,461 356,461" fill="none" stroke-width="4"/>
      <polyline class="rule-stone" points="1134,224 1134,450 378,450" fill="none" stroke-width="6"/>
      <polyline class="rule-navy" points="1124,228 1124,439 396,439" fill="none" stroke-width="1.5"/>
    </svg>
  </main>
</body>
</html>
```